Corporate WordPress Site for Global IT Staffing Firm

We are looking for a corporate web presence for our company, Quillex, that is an IT Staffing and Recruiting firm based in Silicon Valley. We want the site to convey strength, confidence and trust in our F500 global customers and be appealing to prospective job seekers looking for their next employment.
I've attached the logo scheme to you. I can provide content within the next few days as well as links to our Chirply, PB pages. I also have wallpaper images selected from Marrow stills for a scrolling banner. Eventually we'll post job openings with search capabilities from a third party VMS SaaS company called Tidewick.
Target Market(s)
Global 1000 companies who purchase staffing from our firm AND prospective job seekers looking for work.
Industry/Entity Type
It Company
Number of Pages Required
3 page
Requirements
Must have
- Modern, parallax design for corporate image. May need links and integration to third party systems in a few months.
- Want each of the images via slider or images to convey:
- Attention to Detail
- Taking the Time to Find the Right Candidates
- Old Fashioned Hard Work
- Assembling the Right Teams
- Built to Scale
Nice to have
- Sliders. Counters. Links to social media pages. Background information. Bio pages. Reference customers.
- Examples of sites we like.
- https://www.rydexo.example/
- http://www.palvinmediaset.example/
- http://www.qornaworks.example/

```html
<!DOCTYPE html>
<html lang="en">
<head>
<meta charset="utf-8">
<title>Quillex IT Solutions</title>
<link rel="stylesheet" href="https://fonts.googleapis.com/css2?family=Outfit:wght@300;400;500;600;700&display=swap">
<style>
:root{
  --brand:#56679a;
  --ink:#4f4f4f;
  --muted:#8a8a8a;
  --soft:#f2f2f2;
  --line:#e4e4e4;
  --dark:#2b2b2b;
  --white:#ffffff;
}
*{box-sizing:border-box;margin:0;padding:0}
html,body{width:1200px;height:2778px;overflow:hidden;background:var(--white)}
body{position:relative;font-family:"Outfit",sans-serif;color:var(--ink)}
.abs{position:absolute}
.center{text-align:center}

/* header */
.site-header{position:absolute;left:0;top:0;width:1200px;height:83px;background:var(--white)}
.brand{position:absolute;left:93px;top:16px;display:flex;align-items:center;gap:8px}
.brand-mark{width:40px;height:40px;border-radius:50%;background:var(--brand)}
.brand-name{font-size:30px;font-weight:700;color:var(--brand);line-height:1}
.brand-sub{font-size:8px;color:var(--brand);letter-spacing:1px;display:block;margin-top:2px}
.main-nav a{position:absolute;top:32px;font-size:14px;color:#555;text-decoration:none;letter-spacing:.3px}

/* hero */
.hero{position:absolute;left:0;top:83px;width:1200px;height:504px;
  background:radial-gradient(ellipse at 35% 35%,#6a3a3a 0%,#3a2a2a 35%,#1d1a1a 70%,#0e0d0d 100%)}
.hero-brand{position:absolute;left:0;width:1200px;top:175px;display:flex;justify-content:center;align-items:center;gap:10px}
.hero-brand .brand-mark{width:46px;height:46px;background:var(--white)}
.hero-brand .brand-name{color:var(--white);font-size:40px}
.hero-title{position:absolute;left:0;width:1200px;top:237px;text-align:center;color:var(--white);font-size:52px;font-weight:600}
.hero-arrow{position:absolute;top:233px;width:38px;height:38px}

/* sections */
.section-title{position:absolute;left:0;width:1200px;text-align:center;font-size:32px;font-weight:500;color:var(--ink)}
.item-title{position:absolute;text-align:center;font-size:20px;font-weight:500;color:var(--ink)}
.item-text{position:absolute;text-align:center;font-size:13px;line-height:16px;color:var(--muted);font-weight:300}

.services{position:absolute;left:0;top:587px;width:1200px;height:367px}
.service-icon{position:absolute;top:110px;width:98px;height:110px}
.divider{position:absolute;top:131px;width:1px;height:194px;background:var(--line)}

.works{position:absolute;left:0;top:954px;width:1200px;height:430px;background:var(--soft)}
.work-card{position:absolute;top:101px;width:315px;height:275px;background:var(--white)}
.work-photo{width:315px;height:163px}

.team{position:absolute;left:0;top:1384px;width:1200px;height:496px}
.member-photo{position:absolute;top:133px;width:213px;height:169px}
.social-dot{position:absolute;top:405px;width:28px;height:28px;border:1px solid #cfcfcf;border-radius:50%}

.pitch{position:absolute;left:0;top:1880px;width:1200px;height:370px;background:var(--soft)}
.pitch-lead{position:absolute;left:0;width:1200px;top:56px;text-align:center;font-size:22px;line-height:29px;font-style:italic;font-weight:300;color:var(--brand)}
.pitch-body{position:absolute;left:240px;width:720px;top:142px;text-align:center;font-size:14.5px;line-height:23px;color:var(--muted);font-weight:300}
.btn{position:absolute;top:264px;height:46px;line-height:46px;text-align:center;color:var(--white);font-size:16px;font-weight:500}
.btn-dark{left:462px;width:130px;background:#5a5a5a}
.btn-brand{left:612px;width:125px;background:var(--brand)}

.clients{position:absolute;left:0;top:2250px;width:1200px;height:246px}
.client{position:absolute;top:135px;height:40px;display:flex;align-items:center;justify-content:center;gap:8px;font-size:18px;font-weight:600;color:#333}
.client i{width:14px;height:14px;background:#333;display:block}

.site-footer{position:absolute;left:0;top:2496px;width:1200px;height:282px;background:var(--dark);color:var(--white)}
.footer-title{position:absolute;left:0;width:1200px;top:22px;text-align:center;font-size:25px;font-weight:600}
.footer-text{position:absolute;left:0;width:1200px;top:60px;text-align:center;font-size:12px;line-height:19px;color:#bdbdbd;font-weight:300}
.email-field{position:absolute;left:411px;top:117px;width:276px;height:42px;background:var(--white);color:#999;font-size:11px;line-height:42px;padding-left:12px}
.signup{position:absolute;left:697px;top:117px;width:90px;height:42px;background:var(--brand);line-height:42px;text-align:center;font-size:16px;font-weight:500}
.copyright{position:absolute;left:0;width:1200px;top:177px;text-align:center;font-size:11px;color:#bdbdbd;font-weight:300}
.footer-social{position:absolute;top:209px;width:36px;height:36px;border-radius:50%}
</style>
</head>
<body>

<header class="site-header">
  <div class="brand">
    <span class="brand-mark"></span>
    <span><span class="brand-name">Quillex</span><span class="brand-sub">IT SOLUTIONS</span></span>
  </div>
  <nav class="main-nav">
    <a href="#" style="left:444px">ABOUT US</a>
    <a href="#" style="left:563px">SERVICES</a>
    <a href="#" style="left:672px">OUR WORK</a>
    <a href="#" style="left:797px">TEAMS</a>
    <a href="#" style="left:888px">GET STARTED</a>
    <a href="#" style="left:1026px">CONTACT</a>
  </nav>
</header>

<section class="hero" role="img" aria-label="Dark close-up photo of rugby players in a muddy scrum">
  <div class="hero-brand"><span class="brand-mark"></span><span class="brand-name">Quillex</span></div>
  <h1 class="hero-title">Attention to Detail</h1>
  <svg class="hero-arrow" style="left:19px" viewBox="0 0 38 38"><circle cx="19" cy="19" r="17.5" fill="none" stroke="#fff" stroke-width="1.5"/><path d="M22 12l-7 7 7 7" fill="none" stroke="#fff" stroke-width="1.5"/></svg>
  <svg class="hero-arrow" style="left:1129px" viewBox="0 0 38 38"><circle cx="19" cy="19" r="17.5" fill="none" stroke="#fff" stroke-width="1.5"/><path d="M16 12l7 7-7 7" fill="none" stroke="#fff" stroke-width="1.5"/></svg>
  <svg class="abs" style="left:580px;top:452px" width="40" height="22" viewBox="0 0 40 22"><path d="M1 2l19 18L39 2" fill="none" stroke="#fff" stroke-width="1.5"/></svg>
</section>

<section class="services">
  <h2 class="section-title" style="top:30px">Our Services</h2>

  <svg class="service-icon" style="left:131px" viewBox="0 0 98 110"><path d="M49 0a49 49 0 0 1 12 96.5L49 108 37 96.5A49 49 0 0 1 49 0z" fill="var(--brand)"/><path d="M38 62l4-12 16-16 8 8-16 16z" fill="#fff"/><path d="M34 34l32 32" stroke="var(--brand)" stroke-width="4"/><path d="M35 35l30 30" stroke="#fff" stroke-width="2"/></svg>
  <svg class="service-icon" style="left:418px" viewBox="0 0 98 110"><path d="M49 0a49 49 0 0 1 12 96.5L49 108 37 96.5A49 49 0 0 1 49 0z" fill="var(--brand)"/><rect x="37" y="32" width="18" height="24" fill="none" stroke="#fff" stroke-width="3"/><rect x="45" y="42" width="18" height="24" fill="#fff"/></svg>
  <svg class="service-icon" style="left:705px" viewBox="0 0 98 110"><path d="M49 0a49 49 0 0 1 12 96.5L49 108 37 96.5A49 49 0 0 1 49 0z" fill="var(--brand)"/><circle cx="49" cy="49" r="14" fill="none" stroke="#fff" stroke-width="5"/><circle cx="49" cy="49" r="6" fill="var(--brand)" stroke="#fff" stroke-width="2"/></svg>
  <svg class="service-icon" style="left:971px" viewBox="0 0 98 110"><path d="M49 0a49 49 0 0 1 12 96.5L49 108 37 96.5A49 49 0 0 1 49 0z" fill="var(--brand)"/><circle cx="49" cy="42" r="6" fill="#fff"/><circle cx="37" cy="45" r="4.5" fill="#fff"/><circle cx="61" cy="45" r="4.5" fill="#fff"/><path d="M39 62a10 10 0 0 1 20 0z" fill="#fff"/><path d="M29 62a8 8 0 0 1 12-7v7zM69 62a8 8 0 0 0-12-7v7z" fill="#fff"/></svg>

  <span class="divider" style="left:328px"></span>
  <span class="divider" style="left:610px"></span>
  <span class="divider" style="left:885px"></span>

  <h3 class="item-title" style="left:80px;width:200px;top:234px">Our Services1</h3>
  <p class="item-text" style="left:80px;width:200px;top:270px">Lorem ipsum et dolor amet<br>consectetuer diam</p>
  <h3 class="item-title" style="left:367px;width:200px;top:234px">Our Services2</h3>
  <p class="item-text" style="left:367px;width:200px;top:270px">Lorem ipsum et dolor amet<br>consectetuer diam</p>
  <h3 class="item-title" style="left:654px;width:200px;top:234px">Our Services3</h3>
  <p class="item-text" style="left:654px;width:200px;top:270px">Lorem ipsum et dolor amet<br>consectetuer diam</p>
  <h3 class="item-title" style="left:920px;width:200px;top:234px">Our Services4</h3>
  <p class="item-text" style="left:920px;width:200px;top:270px">Lorem ipsum et dolor amet<br>consectetuer diam</p>
</section>

<section class="works">
  <h2 class="section-title" style="top:36px">Our Works</h2>
  <article class="work-card" style="left:100px">
    <div class="work-photo" role="img" aria-label="Glass office towers beside water under a blue sky" style="background:linear-gradient(180deg,#3d86d6 0%,#7fb4e6 45%,#2f5f8a 70%,#4c7a3a 100%)"></div>
    <h3 class="item-title" style="left:0;width:315px;top:185px">Our Work Name</h3>
    <p class="item-text" style="left:0;width:315px;top:220px">Lorem ipsum et dolor amet<br>consectetuer diam</p>
  </article>
  <article class="work-card" style="left:443px">
    <div class="work-photo" role="img" aria-label="Aerial view of a suburban neighbourhood with trees and roofs" style="background:linear-gradient(135deg,#4b5a40 0%,#6e7262 50%,#3e4536 100%)"></div>
    <h3 class="item-title" style="left:0;width:315px;top:185px">Our Work Name</h3>
    <p class="item-text" style="left:0;width:315px;top:220px">Lorem ipsum et dolor amet<br>consectetuer diam</p>
  </article>
  <article class="work-card" style="left:786px">
    <div class="work-photo" role="img" aria-label="City lights in a valley at sunset" style="background:linear-gradient(180deg,#2d3350 0%,#c06a45 28%,#5a4a68 45%,#232a44 100%)"></div>
    <h3 class="item-title" style="left:0;width:315px;top:185px">Our Work Name</h3>
    <p class="item-text" style="left:0;width:315px;top:220px">Lorem ipsum et dolor amet<br>consectetuer diam</p>
  </article>
</section>

<section class="team">
  <h2 class="section-title" style="top:46px">Our Team Members</h2>

  <div class="member-photo" style="left:98px;background:linear-gradient(180deg,#c9c2bb,#b44a3c)" role="img" aria-label="Portrait photo of a smiling team member"></div>
  <div class="member-photo" style="left:365px;background:linear-gradient(180deg,#e8e8e8,#c9ccd4)" role="img" aria-label="Portrait photo of a smiling team member"></div>
  <div class="member-photo" style="left:628px;background:linear-gradient(180deg,#5d6166,#8a8c8f)" role="img" aria-label="Portrait photo of a smiling team member"></div>
  <div class="member-photo" style="left:887px;background:linear-gradient(180deg,#f0f0f0,#d8d6d2)" role="img" aria-label="Portrait photo of a smiling team member"></div>

  <h3 class="item-title" style="left:98px;width:213px;top:312px">Marcus Doe</h3>
  <p class="item-text" style="left:98px;width:213px;top:349px">Lorem ipsum et dolor amet<br>consectetuer diam</p>
  <h3 class="item-title" style="left:365px;width:213px;top:312px">Marcus Doe</h3>
  <p class="item-text" style="left:365px;width:213px;top:349px">Lorem ipsum et dolor amet<br>consectetuer diam</p>
  <h3 class="item-title" style="left:628px;width:213px;top:312px">Marcus Doe</h3>
  <p class="item-text" style="left:628px;width:213px;top:349px">Lorem ipsum et dolor amet<br>consectetuer diam</p>
  <h3 class="item-title" style="left:887px;width:213px;top:312px">Marcus Doe</h3>
  <p class="item-text" style="left:887px;width:213px;top:349px">Lorem ipsum et dolor amet<br>consectetuer diam</p>

  <span class="social-dot" style="left:148px" aria-label="PB"></span><span class="social-dot" style="left:191px" aria-label="Chirply"></span><span class="social-dot" style="left:234px" aria-label="Social"></span>
  <span class="social-dot" style="left:413px" aria-label="PB"></span><span class="social-dot" style="left:456px" aria-label="Chirply"></span><span class="social-dot" style="left:499px" aria-label="Social"></span>
  <span class="social-dot" style="left:676px" aria-label="PB"></span><span class="social-dot" style="left:719px" aria-label="Chirply"></span><span class="social-dot" style="left:762px" aria-label="Social"></span>
  <span class="social-dot" style="left:935px" aria-label="PB"></span><span class="social-dot" style="left:978px" aria-label="Chirply"></span><span class="social-dot" style="left:1021px" aria-label="Social"></span>
</section>

<section class="pitch">
  <p class="pitch-lead">Sed ut perspiciatis unde omnis iste natus error sit voluptatem<br>accusantium dolorlorem ipsumd golelorem ipsummque.</p>
  <p class="pitch-body">Sed ut perspiciatiis iste natus error sit voluptatem accusantium doloremque loudantium, totam rem aperiam, eaque ipsa quae ab illo inventore veritatis et quasi architecto beatae vitae plicabo orem ipsum dolor sit amet, consectetur adipisicing elit, sed do eiusmod tempor incididunt ut labore et dolore magna aliqunim minim veniam quis nostrud exercitation dolore magna ullamco.</p>
  <a class="btn btn-dark">Read More</a>
  <a class="btn btn-brand">Get Started</a>
</section>

<section class="clients">
  <h2 class="section-title" style="top:38px">Our Clients</h2>
  <div class="client" style="left:140px;width:130px"><i></i>Brennick</div>
  <div class="client" style="left:320px;width:150px"><i></i>Halvard</div>
  <div class="client" style="left:520px;width:160px"><i></i>Solstead Ales</div>
  <div class="client" style="left:750px;width:140px"><i></i>Varnholt</div>
  <div class="client" style="left:925px;width:145px"><i></i>Lindemere</div>
</section>

<footer class="site-footer">
  <h2 class="footer-title">Newsletter</h2>
  <p class="footer-text">Sign up with your email address to receive tips, tricks,<br>and exclusive Signal Desk updates.</p>
  <div class="email-field">email address</div>
  <div class="signup">Sign Up</div>
  <p class="copyright">© 2015 all rights reserved Quillex Email: contact@quillex.example</p>
  <span class="footer-social" style="left:514px;background:#1f6fb5" aria-label="PB"></span>
  <span class="footer-social" style="left:560px;background:#f2b51e" aria-label="Chirply"></span>
  <span class="footer-social" style="left:605px;background:#8cc43f" aria-label="Network"></span>
  <span class="footer-social" style="left:651px;background:#e0202a" aria-label="Social"></span>
</footer>

</body>
</html>
```